Business Card Design for anfurniture upcycling business specialisting in rustic, provincial & alpine

I need a business card design for a new aspect of my business called Brush Over Heritage. I upcycle rustic & provincial furniture with beautiful chalk & milk paints, wax & hemp oil to create lovely looking statement pieces. I have also created a range of Alpine décor items using reclaimed wood, chalk &ints & stencils. The alpine theme is carried over into a range of cushions suitable for the alpine apartment/lodge featuring deer, antlers and the names of many key worldwide ski resorts. Small homeware items such as cheese boards &am rack hangers also feature on our web page.I do not have a design in mind or colours, but want the card to convey professionalism, creativity & maybe highlight the alpine theme more, although I do not want people to look at the card, and think that alpine themed furniture and homewares is all there is.

Industry/Entity Type

Business

Contact Information for Business Card

Brush Over HeritageRustic, Provincial & Alpine Themed Furniture & HomewaresContact Lorna - 0478-222-839cwilby@ozemail.com.auwww.facebook.com.au/Brush Over Heritage

Font styles to use
Decorative

Requirements
Must have
• Business name & the types of furniture that I upcycle
• Contact details
• My furniture would be bought by people wanting something different, not the cheap (or expensive) furniture that can be bought anywhere; but by people that want something different in their life
Nice to have
• maybe something that incorporates the three areas I do
Should not have
• Generic - could be any businesses card

```html
<!DOCTYPE html>
<html lang="en">
<head>
<meta charset="utf-8">
<title>Brush Over Heritage – Business Card</title>
<link href="https://fonts.googleapis.com/css2?family=Tinos&family=Source+Sans+3:wght@400&display=swap" rel="stylesheet">
<style>
  :root {
    --page-bg: #e8e5e1;
    --card-white: #ffffff;
    --brand-gold: #c6a52f;
    --panel-grey: #959595;
    --ink: #111111;
    --paper-text: #ffffff;
    --photo-light: #b9b4ad;
    --photo-mid: #8f8a80;
    --photo-warm: #c7a83e;
  }
  html, body {
    margin: 0;
    padding: 0;
    width: 1200px;
    height: 998px;
    overflow: hidden;
    background: var(--page-bg);
  }
  .card {
    position: absolute;
    left: 60px;
    top: 178px;
    width: 1080px;
    height: 641px;
    background: var(--card-white);
    overflow: hidden;
    box-shadow: 0 2px 8px rgba(0,0,0,0.18);
  }
  .card-shapes {
    position: absolute;
    inset: 0;
    width: 100%;
    height: 100%;
  }
  .brand-name,
  .brand-services,
  .contact-name {
    font-family: "Tinos", "Times New Roman", serif;
    position: absolute;
    margin: 0;
    white-space: nowrap;
    font-weight: 400;
  }
  .brand-name {
    right: 29px;
    top: 60px;
    font-size: 50px;
    color: var(--ink);
  }
  .brand-services {
    right: 29px;
    top: 130px;
    font-size: 35px;
    color: var(--ink);
  }
  .contact-name {
    left: 282px;
    top: 420px;
    transform: translateX(-50%);
    font-size: 44px;
    color: var(--paper-text);
  }
  .divider {
    position: absolute;
    left: 496px;
    top: 397px;
    width: 3px;
    height: 163px;
    background: var(--paper-text);
  }
  .contact-list {
    list-style: none;
    margin: 0;
    padding: 0;
    position: absolute;
    left: 582px;
    top: 400px;
    font-family: "Source Sans 3", "Myriad Pro", sans-serif;
    font-size: 27px;
    color: var(--paper-text);
  }
  .contact-item {
    display: flex;
    align-items: center;
    height: 45px;
  }
  .contact-icon {
    width: 22px;
    height: 22px;
    margin-right: 19px;
    flex: none;
  }
  .tagline {
    position: absolute;
    left: 511px;
    top: 595px;
    transform: translateX(-50%);
    margin: 0;
    white-space: nowrap;
    font-family: "Source Sans 3", "Myriad Pro", sans-serif;
    font-size: 27px;
    color: var(--paper-text);
  }
</style>
</head>
<body>
  <div class="card">
    <svg class="card-shapes" viewBox="0 0 1116 662" preserveAspectRatio="none">
      <defs>
        <linearGradient id="photo-tones" x1="0" y1="0" x2="1" y2="1">
          <stop offset="0" stop-color="var(--photo-warm)"/>
          <stop offset="0.35" stop-color="var(--photo-light)"/>
          <stop offset="1" stop-color="var(--photo-mid)"/>
        </linearGradient>
      </defs>
      <rect class="feature-photo" x="0" y="0" width="528" height="400" fill="url(#photo-tones)" role="img" aria-label="Photo of a white jug with yellow lilies beside painted twine spools on a shelf"/>
      <path class="gold-band" d="M0 385 Q 600 368 1116 235 L1116 662 L0 662 Z" fill="var(--brand-gold)"/>
      <path class="grey-panel" d="M0 405 Q 600 392 1116 325 L1116 662 L0 662 Z" fill="var(--panel-grey)"/>
    </svg>

    <h1 class="brand-name">Brush Over Heritage</h1>
    <p class="brand-services">Home decor · Painter · Furniture repair</p>

    <p class="contact-name">Contact Lorna</p>
    <div class="divider"></div>

    <ul class="contact-list">
      <li class="contact-item">
        <svg class="contact-icon" viewBox="0 0 22 22"><rect width="22" height="22" fill="#fff"/><path d="M6 4 L9 4 L10 8 L8 9.5 Q10 13 12.5 14 L14 12 L18 13 L18 16 Q17 18 14 17.5 Q7 15 4.5 7.5 Q4 5 6 4 Z" fill="var(--panel-grey)"/></svg>
        <span>0491-675-304</span>
      </li>
      <li class="contact-item">
        <svg class="contact-icon" viewBox="0 0 22 22"><rect width="22" height="22" fill="#fff"/></svg>
        <span>BrushOverHeritage</span>
      </li>
      <li class="contact-item">
        <svg class="contact-icon" viewBox="0 0 22 22"><rect x="0" y="3" width="22" height="16" fill="#fff"/><path d="M2 5 L11 12 L20 5 M2 17 L8 11 M20 17 L14 11" stroke="var(--panel-grey)" stroke-width="1.6" fill="none"/></svg>
        <span>lmarsh@bluenetmail.com.au</span>
      </li>
      <li class="contact-item">
        <svg class="contact-icon" viewBox="0 0 22 22"><rect width="22" height="22" fill="#fff"/><path d="M11 4 Q16 4 16 9 Q16 12 11 18 Q6 12 6 9 Q6 4 11 4 Z" fill="var(--panel-grey)"/><circle cx="11" cy="9" r="2" fill="#fff"/></svg>
        <span>12 Tarrant St, Kew, Victoria</span>
      </li>
    </ul>

    <p class="tagline">Rustic, Provincial &amp; Alpine Themed&nbsp; Furniture &amp; Homewares</p>
  </div>
</body>
</html>
```